Learn to play polo (that's on horses) business, requires a roadside sign.

We need a signage design for a company based on the edge of Sydney called 'Brenna Polo'. We sell and manage all things polo. We agist horses, breed, train sell polo ponies, provide polo lessons and manage polo ponies for clients. We also sell polo equipment.
We are trying to attract more people to have a go at learning to play polo as we want to build this side of the business. The business owner and polo coach is a previous World Cup captain and professional polo player. Our logo colours are black and white and the logo can be reversed to be white on black. The sign will be placed on the roadside on a direct route into the Sydney CBD. The final design should encompass social, fun, exercise, outdoor themes.

Target Market(s)

Highway traffic including;
Current horse riders or horse lovers (including children aged 12 - 18). It is not essential to have ridden before to partake in our lessons
A and AB socio-economic groups. Some live in the area and work in the CBD, some commute to CBD

Industry/Entity Type

Business

Font styles to use
Sans Serif

Requirements
Must have
• Brenna Polo Pty Ltd
• Learn to Play Polo (or similar)
• www.brennapolo-example.com.au
• 0412 605 298
• Dimensions of sign - 1.5m (w) x 1m (h) Learn to play polo Brenna Polo Pty Ltd www.brennapolo-example.com.au p - 02 9136 2084 m - 0412 605 298
Nice to have
• Themes of social, exercise, excitement, adrenalin.
• Is a sport that offers more. There is scope for family/friends to enjoy beautiful surrounds at the same time as lesson.
Should not have
• Crassness, image that polo lessons are only accessible to elite/ rich.

```html
<!DOCTYPE html>
<html lang="en">
<head>
<meta charset="utf-8">
<title>Brenna Polo – Roadside Sign</title>
<link href="https://fonts.googleapis.com/css2?family=Questrial&family=Caveat:wght@400&display=swap" rel="stylesheet">
<style>
  :root {
    --page: #ffffff;
    --sign: #000000;
    --ink: #ffffff;
    --tree-green: #2e4a22;
    --tree-dark: #1a2a14;
    --horse: #6e3b1f;
    --rider-white: #cfcfc8;
    --field-green: #5f7a45;
  }
  * { margin: 0; padding: 0; box-sizing: border-box; }
  html, body { width: 1200px; height: 1000px; overflow: hidden; background: var(--page); }
  body { position: relative; font-family: "Questrial", "Century Gothic", sans-serif; color: var(--ink); }

  .sign {
    position: absolute; left: 40px; top: 218px; width: 1118px; height: 564px;
    background: var(--sign);
    box-shadow: 3px 4px 6px rgba(0,0,0,0.45);
  }
  .brand-name {
    position: absolute; left: 72px; top: 250px; width: 385px; height: 74px;
    border: 3px solid var(--ink);
    display: flex; align-items: center; justify-content: center;
    font-size: 50px; letter-spacing: 1px; line-height: 1; padding-top: 2px;
  }
  .web-address {
    position: absolute; left: 73px; top: 328px;
    font-size: 21px; letter-spacing: 2.2px; white-space: nowrap;
  }
  .services {
    position: absolute; left: 78px; top: 390px; list-style: none;
    font-size: 33px; line-height: 45px; white-space: nowrap;
  }
  .services li:nth-child(1) { letter-spacing: 15px; }
  .services li:nth-child(2) { letter-spacing: 14.5px; }
  .services li:nth-child(3) { letter-spacing: 14px; }
  .services li:nth-child(4),
  .services li:nth-child(5) { letter-spacing: 8px; }

  .rider-figure {
    position: absolute; left: 66px; top: 652px; width: 86px; height: 98px;
  }
  .contact {
    position: absolute; right: 736px; top: 652px; text-align: right; white-space: nowrap;
  }
  .contact-title { font-size: 23px; letter-spacing: 12px; line-height: 34px; margin-right: -12px; }
  .contact-line { font-size: 24px; letter-spacing: 7.7px; line-height: 35px; margin-right: -7.7px; }

  .tagline {
    position: absolute; left: 520px; top: 254px; width: 590px; text-align: center;
    font-family: "Caveat", cursive; font-size: 52px; letter-spacing: 7px; line-height: 1;
    white-space: nowrap;
  }
  .action-photo {
    position: absolute; left: 498px; top: 300px; width: 614px; height: 386px;
  }
  .headline {
    position: absolute; left: 540px; top: 680px;
    font-size: 43px; letter-spacing: 9.5px; line-height: 1; white-space: nowrap;
  }
  .subline {
    position: absolute; left: 541px; top: 727px;
    font-size: 25px; letter-spacing: 5.7px; line-height: 1; white-space: nowrap;
  }
</style>
</head>
<body>
  <div class="sign"></div>

  <div class="brand-name">BRENNA POLO</div>
  <div class="web-address">www.brennapolo-example.com.au</div>

  <ul class="services">
    <li>Lessons</li>
    <li>Training</li>
    <li>Schooling</li>
    <li>Agistment &amp;</li>
    <li>Equipment Sales.</li>
  </ul>

  <svg class="rider-figure" viewBox="0 0 86 98" role="img" aria-label="White silhouette of a polo player on a galloping horse">
    <ellipse cx="43" cy="70" rx="40" ry="22" fill="#ffffff" opacity="0.85"/>
  </svg>

  <div class="contact">
    <div class="contact-title">Contact us now</div>
    <div class="contact-line">m: 0412 605 298</div>
    <div class="contact-line">ph: 02 9136 2084</div>
  </div>

  <div class="tagline">a sport that offers more</div>

  <svg class="action-photo" viewBox="0 0 614 386" role="img" aria-label="Photo of four riders playing polo on horseback on a green field, trees behind">
    <defs>
      <linearGradient id="sceneTones" x1="0" y1="0" x2="0" y2="1">
        <stop offset="0%" stop-color="var(--tree-dark)"/>
        <stop offset="22%" stop-color="var(--tree-green)"/>
        <stop offset="34%" stop-color="#5a4a38"/>
        <stop offset="46%" stop-color="var(--rider-white)" stop-opacity="0.9"/>
        <stop offset="58%" stop-color="var(--horse)"/>
        <stop offset="76%" stop-color="#5a3320"/>
        <stop offset="90%" stop-color="var(--field-green)"/>
        <stop offset="100%" stop-color="#3d5230"/>
      </linearGradient>
      <radialGradient id="ovalFade" cx="50%" cy="50%" r="50%">
        <stop offset="0%" stop-color="#fff"/>
        <stop offset="72%" stop-color="#fff"/>
        <stop offset="100%" stop-color="#000"/>
      </radialGradient>
      <mask id="ovalMask">
        <ellipse cx="307" cy="193" rx="305" ry="190" fill="url(#ovalFade)"/>
      </mask>
    </defs>
    <rect width="614" height="386" fill="url(#sceneTones)" mask="url(#ovalMask)"/>
  </svg>

  <div class="headline">Learn to Play Polo</div>
  <div class="subline">in a friendly &amp; relaxing setting</div>
</body>
</html>
```